Unique and original Business Card for Financial Services Business

I have moved premises and need to change the detail on my business card so thought now is a good time for a re-design. Looking for something professional and modern with colours to fit in with out logo. Like the idea of foil or embossing if that works but not a must have but I do want something that stands out and that I could not design myself.

Once business card is designed I will also be looking to get letterhead and flyers done but want the business card concept in place first.

The majority of designs I am receiving are generic and template based. I am looking for something unique and original. We have some great design elements in our logo, think outside the box and show me something that stands out from the crowd.

Target Market(s)

Business Professionals

Industry/Entity Type

Finance

Contact Information for Business Card

Name: Delia Norwood Phone 0473 958 162 Address PO Box 8617 Mossvale NSW 2389 Email info@steadyharbourfinancialservices.com.au website www.steadyharbourfinancialservices.com.au

Font styles to use
Other font styles liked:
• Ralway

Requirements
Should not have
• No black backgrounds please

```html
<!DOCTYPE html>
<html lang="en">
<head>
<meta charset="utf-8">
<title>Steady Harbour Financial Services – Business Card</title>
<link rel="stylesheet" href="https://fonts.googleapis.com/css2?family=Open+Sans:wght@400;600;700&display=swap">
<style>
  :root {
    --stage: #000000;
    --front-start: #163a47;
    --front-end: #34545e;
    --teal: #0e9e98;
    --teal-bright: #13aaa0;
    --teal-deep: #06707f;
    --navy: #04283e;
    --ink: #3a3a3d;
    --white: #ffffff;
  }
  * { margin: 0; padding: 0; box-sizing: border-box; }
  html, body { width: 1199px; height: 1200px; overflow: hidden; background: var(--stage); }
  body { position: relative; font-family: "Open Sans", sans-serif; }

  .card {
    position: absolute;
    left: 206px;
    width: 786px;
    height: 449px;
    border-radius: 34px;
    overflow: hidden;
  }

  /* Front */
  .card-front { top: 120px; border: 3px solid var(--teal); }
  .front-pattern {
    position: absolute; inset: 0;
    background: linear-gradient(90deg, var(--front-start) 0%, var(--front-end) 100%);
  }
  .brand { display: flex; align-items: center; gap: 12px; font-weight: 600; }
  .brand-mark { width: 22px; height: 22px; background: var(--teal); flex: none; }
  .brand-text { display: flex; flex-direction: column; align-items: flex-start; line-height: 1.05; }
  .brand-name { font-size: 35px; letter-spacing: -1px; }
  .brand-sub { font-size: 17px; letter-spacing: 8px; }

  .front-brand { position: absolute; right: 44px; bottom: 26px; color: var(--white); }

  /* Back */
  .card-back { top: 618px; background: var(--white); border: 3px solid var(--teal); border-bottom: none; }
  .back-wave { position: absolute; left: 0; top: 0; width: 786px; height: 449px; }
  .back-brand { position: absolute; left: 22px; top: 110px; color: var(--teal); }

  .holder-name {
    position: absolute; right: 36px; top: 38px;
    font-size: 43px; font-weight: 700; letter-spacing: 0.5px; line-height: 1.2;
  }
  .holder-name .first { color: var(--teal-deep); }
  .holder-name .last { color: var(--ink); }
  .name-bar { position: absolute; right: 0; top: 40px; width: 22px; height: 50px; background: linear-gradient(90deg, var(--teal), var(--teal-deep)); }

  .bird-art {
    position: absolute; left: 560px; top: 96px; width: 200px; height: 240px;
    background: linear-gradient(160deg, var(--teal-bright) 0%, var(--teal) 50%, var(--teal-deep) 100%);
    border-radius: 50% 40% 44% 50%;
  }

  .contact-list { position: absolute; left: 22px; top: 258px; list-style: none; }
  .contact-list li {
    display: flex; align-items: center; gap: 13px;
    height: 28.5px; font-size: 19.5px; color: var(--ink);
  }
  .contact-list svg { width: 18px; height: 18px; flex: none; }

  .address {
    position: absolute; left: 444px; width: 300px; top: 372px;
    text-align: center; color: var(--white); font-size: 19.5px; line-height: 28px;
  }
</style>
</head>
<body>

<section class="card card-front" aria-label="Card front">
  <div class="front-pattern" role="img" aria-label="Embossed repeating hummingbird pattern"></div>
  <div class="brand front-brand">
    <span class="brand-mark"></span>
    <div class="brand-text">
      <span class="brand-name">STEADY HARBOUR</span>
      <span class="brand-sub">Financial Services</span>
    </div>
  </div>
</section>

<section class="card card-back" aria-label="Card back">
  <svg class="back-wave" viewBox="0 0 786 449" aria-hidden="true">
    <defs>
      <linearGradient id="waveFill" x1="0" y1="0" x2="1" y2="0">
        <stop offset="0" stop-color="#13aaa0"/>
        <stop offset="0.55" stop-color="#06707f"/>
        <stop offset="1" stop-color="#04283e"/>
      </linearGradient>
      <linearGradient id="swoosh" x1="0" y1="0" x2="1" y2="0">
        <stop offset="0" stop-color="#ffffff"/>
        <stop offset="0.4" stop-color="#8a8a8e"/>
        <stop offset="1" stop-color="#2e2e31"/>
      </linearGradient>
    </defs>
    <path d="M0,385 C110,430 230,440 320,432 C430,420 490,365 570,332 C650,302 720,302 786,300 L786,449 L0,449 Z" fill="url(#waveFill)"/>
    <path d="M0,346 C80,400 200,424 305,418 C200,422 90,400 0,362 Z" fill="url(#swoosh)"/>
  </svg>

  <div class="brand back-brand">
    <span class="brand-mark"></span>
    <div class="brand-text">
      <span class="brand-name">STEADY HARBOUR</span>
      <span class="brand-sub">Financial Services</span>
    </div>
  </div>

  <h1 class="holder-name"><span class="first">Delia</span> <span class="last">Norwood</span></h1>
  <div class="name-bar"></div>

  <div class="bird-art" role="img" aria-label="Teal hummingbird illustration in flight"></div>

  <ul class="contact-list">
    <li>
      <svg viewBox="0 0 24 24"><path d="M6.6 10.8a15 15 0 0 0 6.6 6.6l2.2-2.2a1 1 0 0 1 1-.25 11.4 11.4 0 0 0 3.6.57 1 1 0 0 1 1 1V20a1 1 0 0 1-1 1A17 17 0 0 1 3 4a1 1 0 0 1 1-1h3.5a1 1 0 0 1 1 1c0 1.25.2 2.45.57 3.57a1 1 0 0 1-.25 1z" fill="#06707f"/></svg>
      <span>0473 958 162</span>
    </li>
    <li>
      <svg viewBox="0 0 24 24"><rect x="2" y="5" width="20" height="15" rx="2" fill="none" stroke="#06707f" stroke-width="2.2"/><path d="M3 6l9 7 9-7" fill="none" stroke="#06707f" stroke-width="2.2"/></svg>
      <span>info@steadyharbourfinancialservices.com.au</span>
    </li>
    <li>
      <svg viewBox="0 0 24 24"><circle cx="12" cy="12" r="10" fill="#06707f"/><path d="M7 6c2 1 3 3 2 5s1 3 0 5M15 4c-1 2 1 3 3 3M14 14c2 0 3 2 2 5" fill="none" stroke="#ffffff" stroke-width="1.6"/></svg>
      <span>www.steadyharbourfinancialservices.com.au</span>
    </li>
  </ul>

  <p class="address">PO Box 8617 Mossvale<br>NSW 2389</p>
</section>

</body>
</html>
```